Design of Referral Card for Marlin Storage Group

Card Specifications:
- Size: 4x6 inches
- Format: Two-sided
- Design Style: Simple, eye-catching, and easy to read
CARD DETAILS:
1. Header:
- Main Brand Logo: Display the “Marlin Storage Group” logo prominently at the top center.
2. Referral Information:
- Text Fields:
- Referred By Name: [Blank space for name]
- Referred By Phone Number: [Blank space for phone number]
- Use a clean, legible font and ensure ample space for filling out the information.
3. Facility Logos and Addresses:
- Facility Logos: Include small logos/icons for each facility brand:
- True Harbor Self Storage
- Ned Cardle Self Storage
- Quillan Self Storage
- Ravensmoor Self Storage
- Facility Names and Addresses:
- True Harbor Self Storage: 2753 Quenby Road, Warner Robins, GA 31088
- Ned Cardle Self Storage: 418 Ashgrove Drive, Perry, GA 31069
- Quillan Self Storage:
- 392 N Parson Road, Byron, GA 31008
- 264 S T Halden Sr Pkwy, Byron, GA 31008
- 815 GA-83, Byron, GA 31008
- Ravensmoor Self Storage:
- 728 S Pellam Ridge Blvd, Centerville, GA 31028
- 476 Dorian Kesh Pkwy, Centerville, GA 31028
4. Important Notice:
- Text: “CARD MUST BE PRESENTED AT TIME OF RENTAL FOR DISCOUNT AND REFERRAL FEE DISTRIBUTION”
- Ensure this message is clear and stands out.
5. Website:
- Include the website URL: www.MarlinStorageGroup.example
- Position the website URL at the bottom or in a location that is easy to find.
OTHER DETAILS:
1. Facility Details:
- Organize the addresses for each facility in a clean and easy-to-read format. Use small icons or logos next to each address for visual clarity.
2. Design Elements:
- Layout: Ensure a balanced layout with sufficient space around text and logos to avoid clutter.
- Colors: Use a color scheme that aligns with the brand’s visual identity, maintaining a cohesive look with the front side.
Attachments:
- Marlin Storage Group Logo
- Facility Logos (True Harbor, Ned Cardle, Byron, Centerville)
Objective:
Design a visually appealing referral card that effectively communicates necessary information, including referral details, facility addresses, and important instructions. Ensure the card is simple yet striking, with clear and accessible information for users.
Target Market(s)
People looking for extra space to store their belongings
Industry/Entity Type
Self-Storage

```html
<!DOCTYPE html>
<html lang="en">
<head>
<meta charset="utf-8">
<title>Marlin Storage Group Referral Card</title>
<link rel="stylesheet" href="https://fonts.googleapis.com/css2?family=Poppins:wght@400;500;600;700&family=Saira+Condensed:wght@600;700&display=swap">
<style>
:root{
  --navy:#0d2244;
  --blue:#15a6e6;
  --band-blue:#0aa7e8;
  --white:#ffffff;
  --ring:#c9cbce;
  --ink:#1d2533;
  --page:#f1f2f4;
}
*{box-sizing:border-box;margin:0;padding:0}
html,body{width:1200px;height:2256px;overflow:hidden}
body{background:var(--page);position:relative;font-family:"Poppins",sans-serif}
.card{position:absolute;left:50px;width:1002px;height:668px;transform-origin:0 0;transform:scale(1.0978);overflow:hidden;background:var(--white);box-shadow:0 18px 40px rgba(0,0,0,.14)}
.card--front{top:355px}
.card--back{top:1168px}
.abs{position:absolute}

/* front */
.hero-photo{left:0;top:0;width:1002px;height:558px;background:linear-gradient(90deg,#9ea3a8 0%,#e4e6e8 22%,#f4f5f6 50%,#e2e4e6 78%,#a3a7ab 100%)}
.hero-floor{left:0;top:380px;width:1002px;height:178px;background:linear-gradient(180deg,rgba(200,196,190,0) 0%,rgba(176,170,162,.55) 100%)}
.text-panel{left:0;top:0}
.brand{left:0;width:1002px;top:110px;text-align:center;font-family:"Saira Condensed",sans-serif;font-weight:700;font-size:40px;letter-spacing:1px;color:var(--navy)}
.brand-mark{display:inline-block;width:22px;height:22px;background:var(--navy);margin-right:12px;vertical-align:4px}
.headline{left:0;width:1002px;text-align:center;font-family:"Saira Condensed",sans-serif;font-weight:700;font-size:50px;line-height:1;letter-spacing:1px}
.headline--blue{top:197px;color:var(--blue)}
.headline--navy{top:245px;color:var(--navy)}
.tagline{left:0;width:1002px;top:300px;text-align:center;font-weight:600;font-size:18px;line-height:21px;letter-spacing:.8px;color:var(--ink)}
.front-band{left:0;top:558px;width:1002px;height:110px;background:var(--navy)}
.ref-field{left:57px;width:333px;height:38px;background:var(--white);border-radius:8px;overflow:hidden}
.ref-field--name{top:568px}
.ref-field--phone{top:618px}
.ref-label{left:0;top:0;width:102px;height:38px;background:var(--blue);border-radius:8px;color:var(--white);font-weight:600;font-size:17px;line-height:38px;text-align:center}
.contact{display:flex;align-items:center;color:var(--white)}
.contact svg{flex:none}
.phone{font-weight:400;letter-spacing:.5px}
.url{font-weight:400}

/* back */
.swoosh{left:0;top:0}
.section-title{left:249px;top:60px;font-family:"Saira Condensed",sans-serif;font-weight:700;font-size:32px;letter-spacing:.8px;color:var(--blue)}
.facility-badge{width:122px;height:122px;border:5px solid var(--ring);border-radius:50%;display:flex;align-items:center;justify-content:center;text-align:center;font-family:"Saira Condensed",sans-serif;font-weight:700;font-size:19px;line-height:1.05;color:var(--navy);background:var(--white)}
.pin{width:22px;height:28px}
.address{font-size:13px;line-height:15px;color:var(--ink)}
.address p+p{margin-top:15px}
.notice{left:0;top:466px;width:730px;height:140px;background:var(--navy)}
.notice-text{left:61px;top:486px;font-weight:700;font-size:25px;line-height:36px;color:var(--white);letter-spacing:.4px}
.notice-text .accent{color:var(--blue);font-size:29px}
.contact-band{left:0;top:606px;width:730px;height:62px;background:var(--band-blue)}
.aisle-photo{left:730px;top:0;width:272px;height:668px;background:linear-gradient(180deg,#d9dadb 0%,#b9bbbd 30%,#8e9092 55%,#aaacad 100%)}
</style>
</head>
<body>

<section class="card card--front" aria-label="Referral card front">
  <div class="abs hero-photo" role="img" aria-label="Photo of a bright storage unit aisle with a blue platform cart"></div>
  <div class="abs hero-floor"></div>
  <svg class="abs text-panel" width="1002" height="558" viewBox="0 0 1002 558" aria-hidden="true">
    <polygon points="236,0 770,0 770,330 503,392 236,330" fill="#ffffff" fill-opacity=".55"/>
  </svg>

  <div class="abs brand"><span class="brand-mark"></span>MARLIN STORAGE GROUP</div>
  <div class="abs headline headline--blue">SELF STORAGE IN THE</div>
  <div class="abs headline headline--navy">HEART OF GEORGIA</div>
  <div class="abs tagline">Elevate your storage experience<br>with Marlin Storage Group</div>

  <div class="abs front-band"></div>
  <div class="abs ref-field ref-field--name"><div class="abs ref-label">NAME</div></div>
  <div class="abs ref-field ref-field--phone"><div class="abs ref-label">PHONE</div></div>
  <div class="abs contact" style="left:406px;top:593px;height:40px">
    <svg width="20" height="20" viewBox="0 0 24 24" fill="none" stroke="#15a6e6" stroke-width="1.8" aria-hidden="true"><path d="M5 3h4l2 5-2.5 1.5a11 11 0 0 0 6 6L16 13l5 2v4a2 2 0 0 1-2 2A17 17 0 0 1 3 5a2 2 0 0 1 2-2z"/></svg>
    <span class="phone" style="margin-left:6px;font-size:27px">+1234567890</span>
    <svg style="margin-left:12px" width="20" height="20" viewBox="0 0 24 24" fill="none" stroke="#15a6e6" stroke-width="1.6" aria-hidden="true"><circle cx="12" cy="12" r="10"/><ellipse cx="12" cy="12" rx="4.5" ry="10"/><path d="M2 12h20"/></svg>
    <span class="url" style="margin-left:12px;font-size:18px">www.marlinstoragegroup.example</span>
  </div>
</section>

<section class="card card--back" aria-label="Referral card back">
  <svg class="abs swoosh" width="240" height="160" viewBox="0 0 240 160" aria-hidden="true">
    <path d="M0 150 C40 110 120 82 215 78 C130 84 50 105 0 124 Z" fill="#15a6e6"/>
  </svg>
  <h2 class="abs section-title">OUR LOCATION</h2>

  <div class="abs facility-badge" style="left:66px;top:129px">True<br>Harbor</div>
  <svg class="abs pin" style="left:201px;top:176px" viewBox="0 0 22 28" fill="none" stroke="#15a6e6" stroke-width="1.8" aria-hidden="true"><path d="M11 27s9-9 9-16a9 9 0 0 0-18 0c0 7 9 16 9 16z"/><circle cx="11" cy="11" r="3"/></svg>
  <div class="abs address" style="left:233px;top:172px"><p>2753 Quenby Road,<br>Warner Robins, GA<br>31088</p></div>

  <div class="abs facility-badge" style="left:405px;top:129px">Ned<br>Cardle</div>
  <svg class="abs pin" style="left:539px;top:176px" viewBox="0 0 22 28" fill="none" stroke="#15a6e6" stroke-width="1.8" aria-hidden="true"><path d="M11 27s9-9 9-16a9 9 0 0 0-18 0c0 7 9 16 9 16z"/><circle cx="11" cy="11" r="3"/></svg>
  <div class="abs address" style="left:574px;top:172px"><p>418 Ashgrove<br>Drive, Perry, GA<br>31069</p></div>

  <div class="abs facility-badge" style="left:64px;top:273px">Quillan</div>
  <svg class="abs pin" style="left:199px;top:302px" viewBox="0 0 22 28" fill="none" stroke="#15a6e6" stroke-width="1.8" aria-hidden="true"><path d="M11 27s9-9 9-16a9 9 0 0 0-18 0c0 7 9 16 9 16z"/><circle cx="11" cy="11" r="3"/></svg>
  <div class="abs address" style="left:232px;top:300px">
    <p>392 N Parson Road,<br>Byron, GA 31008</p>
    <p>264 S T Halden Sr<br>Pkwy, Byron, GA<br>31008</p>
    <p>815 GA-83, Byron,<br>GA 31008</p>
  </div>

  <div class="abs facility-badge" style="left:405px;top:273px">Ravens-<br>moor</div>
  <svg class="abs pin" style="left:539px;top:318px" viewBox="0 0 22 28" fill="none" stroke="#15a6e6" stroke-width="1.8" aria-hidden="true"><path d="M11 27s9-9 9-16a9 9 0 0 0-18 0c0 7 9 16 9 16z"/><circle cx="11" cy="11" r="3"/></svg>
  <div class="abs address" style="left:572px;top:316px">
    <p>728 S Pellam Ridge<br>Blvd, Centerville,<br>GA 31028</p>
    <p>476 Dorian Kesh<br>Pkwy, Centerville,<br>GA 31028</p>
  </div>

  <div class="abs notice"></div>
  <div class="abs notice-text">CARD MUST BE PRESENTED AT TIME OF<br>RENTAL FOR <span class="accent">DISCOUNT</span> AND REFERRAL<br><span class="accent">FEE DISTRIBUTION</span></div>

  <div class="abs contact-band"></div>
  <div class="abs contact" style="left:57px;top:617px;height:40px">
    <svg width="20" height="20" viewBox="0 0 24 24" fill="none" stroke="#ffffff" stroke-width="1.8" aria-hidden="true"><path d="M5 3h4l2 5-2.5 1.5a11 11 0 0 0 6 6L16 13l5 2v4a2 2 0 0 1-2 2A17 17 0 0 1 3 5a2 2 0 0 1 2-2z"/></svg>
    <span class="phone" style="margin-left:6px;font-size:25px">+1234567890</span>
    <svg style="margin-left:12px" width="20" height="20" viewBox="0 0 24 24" fill="none" stroke="#ffffff" stroke-width="1.6" aria-hidden="true"><circle cx="12" cy="12" r="10"/><ellipse cx="12" cy="12" rx="4.5" ry="10"/><path d="M2 12h20"/></svg>
    <span class="url" style="margin-left:14px;font-size:17px">www.marlinstoragegroup.example</span>
  </div>

  <div class="abs aisle-photo" role="img" aria-label="Black and white photo of a long indoor storage corridor lined with roll-up doors"></div>
</section>

</body>
</html>
```